Business Card Design Project

Basic business card with minimal details. I just need company name, email & web address, telephone and my name.
I would like the back of the card to be grey with my logo & company name centred.

Target Market(s)

Architects
Builders
Property Developers

Industry/Entity Type

Business

Font styles to use
Sans Serif

Colors

Designer to choose colors to be used in the design.

Requirements
Must have
• Framewise Build
Marcus Helby - Director
M: 0427 593184
E: marcus@framewisebuild.com.au
W: www.framewisebuild.com.au
Should not have
• No other images or pictures

```html
<!DOCTYPE html>
<html lang="en">
<head>
<meta charset="utf-8">
<title>Framewise Build — Business Card</title>
<link rel="stylesheet" href="https://fonts.googleapis.com/css2?family=Lato:wght@400;700&display=swap">
<style>
  :root {
    --backdrop: #e8e5e1;
    --card-black: #0c0c0d;
    --card-grey: #45484d;
    --card-white: #ffffff;
    --crimson: #b8163b;
    --slate: #6d7884;
    --slate-light: #c9d0d8;
    --ink-light: #f2f2f2;
    --ink-muted: #a9b0b8;
    --card-w: 540px;
    --card-h: 309px;
  }
  * { margin: 0; padding: 0; box-sizing: border-box; }
  html, body {
    width: 1200px; height: 800px; overflow: hidden;
    background: var(--backdrop);
    font-family: "Lato", Arial, sans-serif;
  }
  .canvas {
    position: relative; width: 1200px; height: 800px;
    display: flex; align-items: center; justify-content: center; gap: 40px;
  }
  .card {
    position: relative; width: var(--card-w); height: var(--card-h);
    overflow: hidden; box-shadow: 0 10px 28px rgba(0,0,0,0.18);
  }
  .card-back { background: var(--card-grey); }
  .card-front { background: var(--card-black); }
  .card-art { position: absolute; inset: 0; width: 100%; height: 100%; }

  .brand {
    position: absolute; display: flex; align-items: center;
    color: var(--slate); font-weight: 400; text-transform: uppercase;
    letter-spacing: 0.08em; white-space: nowrap;
  }
  .brand-square { display: block; background: var(--crimson); flex: none; }

  .card-back .brand {
    left: 50%; top: 50%; transform: translate(-50%, -50%);
    font-size: 28px; gap: 16px; color: var(--slate-light);
  }
  .card-back .brand-square { width: 26px; height: 26px; }

  .card-front .brand { left: 50%; top: 74px; transform: translateX(-50%); font-size: 21px; gap: 12px; }
  .card-front .brand-square { width: 20px; height: 20px; }

  .holder {
    position: absolute; left: 34px; bottom: 22px;
  }
  .holder-name {
    color: var(--crimson); font-size: 24px; font-weight: 400; line-height: 28px;
  }
  .holder-title {
    color: var(--ink-muted); font-size: 12.5px; font-weight: 400;
    letter-spacing: 0.12em; text-transform: uppercase; line-height: 18px;
  }
  .contact-list {
    position: absolute; left: 318px; top: 168px; list-style: none;
    color: var(--ink-light); font-size: 12.5px; line-height: 21px;
  }
  .contact-list li { display: flex; align-items: center; gap: 9px; }
  .contact-icon { width: 11px; height: 11px; flex: none; }
</style>
</head>
<body>
<main class="canvas">

  <section class="card card-back" aria-label="Card back">
    <div class="brand">
      <span class="brand-square"></span>
      <span class="brand-name">Framewise Build</span>
    </div>
  </section>

  <section class="card card-front" aria-label="Card front">
    <svg class="card-art" viewBox="0 0 540 309" preserveAspectRatio="none" aria-hidden="true">
      <polygon points="0,0 540,0 540,72 0,222" fill="var(--card-white)"/>
      <polygon points="0,222 540,72 540,88 0,238" fill="var(--crimson)"/>
    </svg>

    <div class="brand">
      <span class="brand-square"></span>
      <span class="brand-name">Framewise Build</span>
    </div>

    <ul class="contact-list">
      <li>
        <svg class="contact-icon" viewBox="0 0 12 12" aria-hidden="true"><path d="M2.5 1h2l1 3-1.3 1a7 7 0 0 0 2.8 2.8l1-1.3 3 1v2a1.5 1.5 0 0 1-1.5 1.5A9.5 9.5 0 0 1 1 2.5 1.5 1.5 0 0 1 2.5 1z" fill="var(--crimson)"/></svg>
        <span>0427 593184</span>
      </li>
      <li>
        <svg class="contact-icon" viewBox="0 0 12 12" aria-hidden="true"><rect x="0.5" y="2" width="11" height="8" fill="var(--crimson)"/><path d="M0.8 2.4 6 6.6l5.2-4.2" fill="none" stroke="var(--card-black)" stroke-width="1"/></svg>
        <span>marcus@framewisebuild.com.au</span>
      </li>
      <li>
        <svg class="contact-icon" viewBox="0 0 12 12" aria-hidden="true"><circle cx="6" cy="6" r="5" fill="none" stroke="var(--crimson)" stroke-width="1.3"/><path d="M1 6h10M6 1c-2.6 2.8-2.6 7.2 0 10M6 1c2.6 2.8 2.6 7.2 0 10" fill="none" stroke="var(--crimson)" stroke-width="1"/></svg>
        <span>www.framewisebuild.com.au</span>
      </li>
    </ul>

    <div class="holder">
      <p class="holder-name">Marcus Helby</p>
      <p class="holder-title">Director</p>
    </div>
  </section>

</main>
</body>
</html>
```